Wordpress website design for a high-end painting business

We are currently rebranding and are looking to update our Wordpress theme. We have recently rebranded our logo on ArtHatchery, and would like our website to be equally as refined.
Our business is named “Holloway Coatings”. We are a high-end painting business that is known for being professional and having high standards. Our clean and professional image is important as it separates us from our competition. Our current website can be found at www.hollowayfinishes.co.nz . We designed the site ourselves so it is understandably rudimentary. We are generally happy with the. page layout of our existing site, but we like a professional remodel. Any ideas on improvement welcomed.
We would like the front page of the website to summarise all of the info throughout the whole website (I.e introduction, photos, testimonials, contact info etc.) as visitors typically scroll through the first page to see that we are reputable and get to our contact number/email contact at the bottom of the page. We would like this first page to give a clean well rounded image of our business. We would like the gallery to be a scroll through of large photos, as it is difficult to see paint details in smaller photos. A contact page with an enquiry section would also be good.
For the colour scheme, we would like something that fits a bold, masculine and high end theme (similar to our logo attached).
We would like the footer to include Velnor paint logos and the accredited painter logo we have included as these are important to our profession.
We have attached some photos of our work also. I will add more in the coming days. More can also be found on our website.
If you have questions or comments, please don’t hesitate to ask and I will get back as soon as possible.
We are open to your own interpretation or ideas for a better layout/site provided they fit the general brief of being a well rounded site for our profession.
Thanks,
Holloway Coatings.
Target Market(s)
High end clients
Industry/Entity Type
Painting (interior and exterior)
Coding
Coded - Design and coding required
Requirements
Must have
- Classy feel, separating us from typical painting companies. Well rounded homepage.
Nice to have
- Lots of examples of our work
Should not have
- Untidy paint motifs (eg, paint droplets, paint splashes)

```html
<!DOCTYPE html>
<html lang="en">
<head>
<meta charset="utf-8">
<title>Holloway Coatings – Home</title>
<link href="https://fonts.googleapis.com/css2?family=Roboto+Slab:wght@300;400;500;600;700&display=swap" rel="stylesheet">
<style>
:root{
  --brown:#8a6a45;
  --brown-dark:#6f5434;
  --brown-soft:#a88a64;
  --ink:#111;
  --black:#000;
  --paper:#fff;
  --card:#f6f4f1;
}
*{box-sizing:border-box;margin:0;padding:0}
html,body{width:1200px;height:5305px;overflow:hidden}
body{position:relative;background:var(--paper);font-family:"Roboto Slab",Georgia,serif;color:var(--ink)}
.abs{position:absolute}
svg.layer{position:absolute;left:0;display:block}

/* header */
.phone-top{left:128px;top:34px;font-size:13px;color:var(--brown);font-weight:600;display:flex;align-items:center;gap:8px}
.icon-dot{width:22px;height:22px;border-radius:50%;background:var(--brown);display:inline-flex;align-items:center;justify-content:center;flex:none}
.nav a{position:absolute;top:90px;font-size:13px;font-weight:600;color:var(--ink);text-decoration:none;text-transform:uppercase}
.nav a.active{color:var(--brown)}
.brand{left:487px;top:22px;width:200px;text-align:center}
.brand-mark{width:66px;height:66px;border-radius:50%;background:var(--brown);margin:0 auto 10px}
.brand-name{font-size:19px;font-weight:600;color:var(--ink);letter-spacing:1px;line-height:1.1}
.brand-sub{font-size:11px;letter-spacing:3px;color:var(--ink)}
.round-btn{border-radius:50%;background:var(--brown);color:#fff;display:flex;align-items:center;justify-content:center;text-align:center;font-weight:600;text-transform:uppercase}
.search-btn{left:928px;top:12px;width:62px;height:62px}
.enquire-btn{left:1000px;top:12px;width:62px;height:62px;font-size:9px;line-height:1.2}

/* hero */
.hero-faint{left:0;top:380px;width:560px;height:440px;background:radial-gradient(ellipse at 35% 55%,#e6e6e6 0%,#f3f3f3 40%,rgba(255,255,255,0) 72%)}
.hero-title{left:132px;top:322px;font-size:37px;font-weight:700;line-height:1.2;text-transform:uppercase}
.hero-title span{color:var(--brown)}
.hero-lead{left:132px;top:428px;font-size:21px;line-height:1.35;width:370px}
.hero-more{left:132px;top:504px;width:100px;height:100px;font-size:17px;line-height:1.15}
.hero-ring{left:522px;top:234px;width:546px;height:546px;border-radius:50%;border:8px solid #e9e9e9}
.hero-photo{left:540px;top:252px;width:510px;height:510px;border-radius:50%;
  background:
    linear-gradient(180deg,rgba(0,0,0,0) 0 62%,#4f5f34 62% 100%),
    linear-gradient(180deg,rgba(0,0,0,0) 0 30%,#e8e4d6 30% 62%,rgba(0,0,0,0) 62%),
    linear-gradient(180deg,#dfe7ee 0%,#c7d2dc 30%,#fff 100%)}

/* services */
.services-title{left:129px;top:963px;font-size:40px;font-weight:700;color:#fff;text-transform:uppercase}
.service{position:absolute;top:1080px;width:240px;text-align:center;color:#fff}
.service-photo{width:200px;height:200px;border-radius:50%;margin:0 auto;border:4px solid var(--brown);position:relative}
.service-badge{position:absolute;left:70px;bottom:-22px;width:52px;height:52px;border-radius:50%;background:var(--brown);border:3px solid #fff;display:flex;align-items:center;justify-content:center}
.service h3{margin-top:38px;font-size:15px;font-weight:600;text-transform:uppercase}
.service p{margin-top:10px;font-size:12px;line-height:1.35;color:#ddd}
.arrow{position:absolute;top:1166px}

/* about */
.about-bg{left:0;top:1530px;width:1200px;height:800px;background:linear-gradient(180deg,#e3e8f2 0%,#f4f5f8 60%,#fff 100%)}
.about-ring{left:96px;top:1728px;width:316px;height:316px;border-radius:50%;border:3px solid var(--brown)}
.about-photo{left:113px;top:1745px;width:282px;height:282px;border-radius:50%;
  background:
    linear-gradient(180deg,rgba(0,0,0,0) 0 70%,#6f7a62 70%),
    linear-gradient(180deg,#b9c7d6 0%,#8c96a2 40%,#50545a 70%)}
.about-figure{left:60px;top:1820px;width:210px;height:200px;border-radius:50%;background:radial-gradient(circle,rgba(138,106,69,.85) 0%,rgba(138,106,69,.5) 55%,rgba(138,106,69,0) 72%)}
.about-title{left:658px;top:1710px;font-size:40px;font-weight:700;text-transform:uppercase;color:var(--ink)}
.about-title span{color:var(--brown)}
.about-text{left:658px;top:1773px;width:420px;font-size:13.4px;line-height:1.55;color:#333}
.about-text p+p{margin-top:18px}
.about-more{left:655px;top:2082px;width:90px;height:90px;font-size:14px;line-height:1.15}

/* call to action */
.cta-text{left:128px;top:2470px;color:#fff}
.cta-text .q{font-size:27px;font-weight:500;line-height:1.28;text-transform:uppercase}
.cta-text .call{margin-top:25px;font-size:27px;font-weight:500}
.cta-text .num{font-size:40px;font-weight:600;margin-top:4px}
.cta-btn{left:788px;top:2566px;width:142px;height:142px;border:2px solid #fff;background:transparent;font-size:20px;line-height:1.25;color:#fff}

/* works */
.works-title{left:0;top:2974px;width:1200px;text-align:center;font-size:40px;font-weight:700;text-transform:uppercase}
.works-title span,.test-title span{color:var(--brown)}
.work{position:absolute;border-radius:50%}
.dots{position:absolute;display:flex;gap:8px}
.dots i{width:13px;height:13px;border-radius:50%;background:#9c9c9c;display:block}
.dots.small i{width:11px;height:11px;background:#c8c8c8}

/* testimonials */
.test-title{left:0;top:3740px;width:1200px;text-align:center;font-size:40px;font-weight:700;text-transform:uppercase}
.test-card{position:absolute;top:3888px;width:295px;height:322px;border:1px solid #d9cbb8;border-radius:148px 148px 0 0;background:var(--card);padding:56px 36px 0}
.quote-mark{position:absolute;top:3848px;width:50px;height:50px;border-radius:50%;background:var(--brown);display:flex;align-items:center;justify-content:center;color:#fff;font-size:40px;font-weight:700;line-height:1;padding-top:14px}
.who{display:flex;align-items:center;gap:14px}
.avatar{width:66px;height:66px;border-radius:50%;background:#777;flex:none}
.who b{display:block;font-size:12px;font-weight:500;color:#555}
.who small{font-size:11px;color:#aaa}
.test-card p{margin-top:22px;font-size:12px;line-height:1.4;color:#9a9a9a}
.dot-grid{left:100px;top:4160px;width:40px;height:70px;background-image:radial-gradient(#b59a76 1.5px,transparent 1.6px);background-size:8px 8px}

/* quote form */
.form-title{left:0;top:4507px;width:1200px;text-align:center;color:#fff;font-size:40px;font-weight:600;text-transform:uppercase}
.field{position:absolute;border:2px solid #fff;border-radius:26px;color:#fff;font-size:16px;padding:13px 18px}
.field.line{left:288px;width:334px;height:50px}
.field.msg{left:644px;top:4592px;width:376px;height:202px;border-radius:70px;padding:16px 62px}
.submit{left:940px;top:4734px;width:84px;height:84px;background:#fff;color:var(--brown);font-size:14px;line-height:1.15}

/* footer */
.foot-brand{left:124px;top:4960px;width:200px;text-align:center;color:#fff}
.foot-brand .brand-mark{width:120px;height:120px;margin-bottom:22px}
.foot-brand .brand-name{color:#fff;font-size:30px;font-weight:500;letter-spacing:1px;line-height:1.15}
.foot-head{font-size:22px;color:var(--brown);font-weight:500;text-transform:uppercase}
.contact-list{left:442px;top:5030px;color:#fff;font-size:15px}
.contact-list li{list-style:none;display:flex;gap:16px;align-items:center;position:absolute;white-space:nowrap}
.contact-list .icon-dot{width:28px;height:28px}
.partner{position:absolute;height:42px;border-radius:3px}
.social{position:absolute;top:5160px;width:30px;height:30px;border-radius:50%;background:var(--brown)}
.copyright{left:0;top:5262px;width:1200px;height:43px;background:var(--brown);color:#fff;font-size:15px;display:flex;align-items:center;justify-content:center}
</style>
</head>
<body>

<!-- header -->
<div class="abs phone-top"><span class="icon-dot"><svg width="12" height="12" viewBox="0 0 24 24"><path fill="#fff" d="M6.6 10.8a15 15 0 0 0 6.6 6.6l2.2-2.2c.3-.3.7-.4 1-.2 1.1.4 2.3.6 3.6.6.6 0 1 .4 1 1V20c0 .6-.4 1-1 1A17 17 0 0 1 3 4c0-.6.4-1 1-1h3.5c.6 0 1 .4 1 1 0 1.3.2 2.5.6 3.6.1.3 0 .7-.2 1z"/></svg></span>PHONE: 022 555 0148</div>
<nav class="nav">
  <a class="active" style="left:142px">Home</a>
  <a style="left:229px">Our Services</a>
  <a style="left:383px">Gallery</a>
  <a style="left:720px">About</a>
  <a style="left:821px">Contact</a>
  <a style="left:942px">Testimonials</a>
</nav>
<div class="abs brand">
  <div class="brand-mark"></div>
  <div class="brand-name">HOLLOWAY</div>
  <div class="brand-sub">COATINGS</div>
</div>
<div class="abs round-btn search-btn"><svg width="14" height="14" viewBox="0 0 24 24"><circle cx="10" cy="10" r="6" fill="none" stroke="#fff" stroke-width="3"/><path d="M15 15l6 6" stroke="#fff" stroke-width="3"/></svg></div>
<div class="abs round-btn enquire-btn">Enquire<br>Here</div>

<!-- hero -->
<div class="abs hero-faint" role="img" aria-label="Faint grey classical statue in the background"></div>
<h1 class="abs hero-title">Welcome to<br><span>Holloway Coatings</span></h1>
<p class="abs hero-lead">Here at Holloway Coatings, we take a lot of pride in our work.</p>
<div class="abs round-btn hero-more">Read<br>More</div>
<div class="abs hero-ring"></div>
<div class="abs hero-photo" role="img" aria-label="Photo of a freshly painted single-storey house with a lawn"></div>

<!-- services band -->
<svg class="layer" style="top:780px" width="1200" height="790" viewBox="0 0 1200 790">
  <path d="M0 20 C150 0 280 20 420 100 C560 180 640 180 760 120 C900 40 1040 60 1200 130 L1200 735 L1100 742 L1000 735 L880 745 L760 736 L620 744 L480 738 L340 746 L200 737 L80 745 L0 738 Z" fill="#000"/>
</svg>
<h2 class="abs services-title">Our Services</h2>
<svg class="arrow" style="left:50px" width="24" height="36" viewBox="0 0 24 36"><path d="M18 4L5 18l13 14" fill="none" stroke="#fff" stroke-width="4"/></svg>
<svg class="arrow" style="left:1110px" width="24" height="36" viewBox="0 0 24 36"><path d="M6 4l13 14L6 32" fill="none" stroke="#fff" stroke-width="4"/></svg>

<div class="service" style="left:108px"><div class="service-photo" role="img" aria-label="Photo of a painted two-storey house exterior" style="background:linear-gradient(180deg,#a9cbea 0 35%,#e6e3dc 35% 62%,#5d5d5d 62% 72%,#6c7f4a 72%)"><span class="service-badge"><svg width="24" height="22" viewBox="0 0 24 22"><path d="M2 11L12 2l10 9M5 9v11h14V9" fill="none" stroke="#fff" stroke-width="2"/></svg></span></div><h3>Exterior Painting</h3><p>Lorem ipsum dolor sit amet, consectetur adipiscing elit, sed do eiusmod tempor incid</p></div>
<div class="service" style="left:353px"><div class="service-photo" role="img" aria-label="Photo of a freshly painted interior room" style="background:linear-gradient(180deg,#f0ede7 0 60%,#8f7a66 60%)"><span class="service-badge"><svg width="24" height="22" viewBox="0 0 24 22"><path d="M2 11L12 2l10 9M5 9v11h14V9M9 20v-6h6v6" fill="none" stroke="#fff" stroke-width="2"/></svg></span></div><h3>Interior Painting</h3><p>Lorem ipsum dolor sit amet, consectetur adipiscing elit, sed do eiusmod tempor incid</p></div>
<div class="service" style="left:598px"><div class="service-photo" role="img" aria-label="Photo of a patterned wallpapered wall" style="background:linear-gradient(90deg,#e4e2dc 0 30%,#8e8f86 30% 75%,#d8d6d0 75%)"><span class="service-badge"><svg width="20" height="22" viewBox="0 0 20 22"><rect x="2" y="2" width="16" height="7" rx="2" fill="none" stroke="#fff" stroke-width="2"/><path d="M10 9v11" stroke="#fff" stroke-width="3"/></svg></span></div><h3>Wallpapering</h3><p>Lorem ipsum dolor sit amet, consectetur adipiscing elit, sed do eiusmod tempor incid</p></div>
<div class="service" style="left:843px"><div class="service-photo" role="img" aria-label="Photo of a hand plastering a wall with a trowel" style="background:linear-gradient(135deg,#f2f2f2 0 35%,#7a7a7a 35% 55%,#d59a76 55% 80%,#f2f2f2 80%)"><span class="service-badge"><svg width="22" height="20" viewBox="0 0 22 20"><rect x="2" y="2" width="18" height="16" fill="none" stroke="#fff" stroke-width="2"/><path d="M2 10h18M11 2v16" stroke="#fff" stroke-width="2"/></svg></span></div><h3>Plastering</h3><p>Lorem ipsum dolor sit amet, consectetur adipiscing elit, sed do eiusmod tempor incid</p></div>

<!-- about -->
<div class="abs about-bg" style="z-index:-1"></div>
<div class="abs about-ring"></div>
<div class="abs about-photo" role="img" aria-label="Photo of a painted modern house"></div>
<div class="abs about-figure" role="img" aria-label="Bronze archer illustration in front of the house photo"></div>
<h2 class="abs about-title"><span>About</span> Us</h2>
<div class="abs about-text">
  <p>Here at Holloway Coatings, we take a lot of pride in our work. We strive to ensure the highest quality paint-work, paying close attention to detail to provide a long lasting finish. Our clients are always our priority, we aim to deliver beyond their expectations. It is our goal to provide an excellent service from start to finish through clear communication, free quoting and transparency with our pricing.</p>
  <p>We take great pride in the preparation of surfaces for painting and only use the best quality products to ensure we achieve the best finish for you. Our qualified interior designer can also assist you with your colour selection as a part of our free colour consultancy service.</p>
</div>
<div class="abs round-btn about-more">Read<br>More</div>

<!-- call to action -->
<svg class="layer" style="top:2265px" width="1200" height="760" viewBox="0 0 1200 760" role="img" aria-label="Faded photo of a painted villa with a brown overlay">
  <defs><linearGradient id="ctaFill" x1="0" y1="0" x2="0" y2="1"><stop offset="0" stop-color="#a89274"/><stop offset=".35" stop-color="#8f7555"/><stop offset=".6" stop-color="#7e6141"/><stop offset="1" stop-color="#8a6c4a"/></linearGradient></defs>
  <path d="M0 90 C200 130 420 140 640 110 C860 80 1060 40 1200 0 L1200 750 C1050 700 880 620 720 580 C560 540 460 530 320 540 C180 550 80 570 0 570 Z" fill="url(#ctaFill)"/>
</svg>
<div class="abs cta-text">
  <div class="q">If you are looking at painting<br>your property, or have any questions,</div>
  <div class="call">Please don’t hesitate to call Rowan</div>
  <div class="num">on 022 5550148.</div>
</div>
<div class="abs round-btn cta-btn">Get<br>a Free<br>Quote</div>

<!-- works -->
<div class="abs" style="left:0;top:3040px;width:1200px;height:660px;background:linear-gradient(180deg,#fff 0%,#f0f1f4 100%);z-index:-1"></div>
<h2 class="abs works-title"><span>Our</span> Works</h2>
<div class="work" role="img" aria-label="Photo of a painted weatherboard house corner" style="left:40px;top:3112px;width:166px;height:166px;background:linear-gradient(180deg,#a9c7e3 0 40%,#e9e6e0 40% 70%,#6d5844 70%)"></div>
<div class="work" role="img" aria-label="Photo of an interior living room" style="left:222px;top:3112px;width:166px;height:166px;background:linear-gradient(180deg,#e2ddd4 0 58%,#3f332b 58% 70%,#8a7563 70%)"></div>
<div class="work" role="img" aria-label="Photo of a white kitchen" style="left:40px;top:3293px;width:166px;height:166px;background:linear-gradient(90deg,#f4f2ee 0 45%,#3b332d 45% 60%,#ece9e3 60%)"></div>
<div class="work" role="img" aria-label="Photo of a cream painted cottage" style="left:222px;top:3293px;width:166px;height:166px;background:linear-gradient(180deg,#cfe0ee 0 38%,#ece7d7 38% 70%,#6f8a4a 70%)"></div>
<div class="work" role="img" aria-label="Photo of a large painted brick and weatherboard house" style="left:402px;top:3076px;width:398px;height:398px;background:linear-gradient(180deg,#7fb0de 0 30%,#dfe1e2 30% 55%,#8b4a35 55% 80%,#4a4a42 80%)"></div>
<div class="work" role="img" aria-label="Photo of a dark painted house with driveway" style="left:810px;top:3112px;width:166px;height:166px;background:linear-gradient(180deg,#3d79c2 0 45%,#2f2f2f 45% 62%,#8d8d8d 62%)"></div>
<div class="work" role="img" aria-label="Photo of a patterned wallpaper wall" style="left:992px;top:3112px;width:166px;height:166px;background:linear-gradient(90deg,#cfccc4 0 25%,#7f8078 25% 75%,#d6d4cc 75%)"></div>
<div class="work" role="img" aria-label="Photo of a grey painted house side" style="left:810px;top:3293px;width:166px;height:166px;background:linear-gradient(180deg,#a6bfd8 0 35%,#6c6f78 35% 78%,#48433b 78%)"></div>
<div class="work" role="img" aria-label="Photo of a white painted home with lawn" style="left:992px;top:3293px;width:166px;height:166px;background:linear-gradient(180deg,#6a9ad0 0 42%,#e5e7ea 42% 68%,#5d7b3b 68%)"></div>
<div class="dots" style="left:546px;top:3537px"><i></i><i></i><i></i><i></i><i></i></div>
<svg class="layer" style="top:3600px" width="1200" height="110" viewBox="0 0 1200 110"><path d="M0 0 L1200 0 L1200 30 C900 80 500 100 0 60 Z" fill="#f0f1f4"/></svg>

<!-- testimonials -->
<h2 class="abs test-title"><span>Client</span> Testimonials</h2>
<div class="abs dot-grid"></div>
<div class="test-card" style="left:130px">
  <div class="who"><span class="avatar"></span><div><b>Martin Cole</b><small>(2020)</small></div></div>
  <p>Just had our house interior painted throughout by Holloway. They were professional right from the start. They turned up to give a quote when other firms never responded. They were spot on with their time and cost estimates and never missed a day ..we had to ask them not to work on Public Holidays.</p>
</div>
<div class="test-card" style="left:453px">
  <div class="who"><span class="avatar"></span><div><b>Daniel</b><small>(August, 2017)</small></div></div>
  <p>These guys are great from beginning to end. Very professional, excellent businessmen, hard workers, and top-quality work. Excellent communication, do what they say they will do and more, and really go the extra mile to make the job as painless as possible</p>
</div>
<div class="test-card" style="left:776px">
  <div class="who"><span class="avatar"></span><div><b>Helen</b><small>(June, 2018)</small></div></div>
  <p>If anyone is looking for a painter, I can highly recommend Holloway Coatings &amp; Decorators. Rowan has just finished repainting the inside of our home and we have been very impressed with his workmanship, attention to detail, communication and respect for our family.</p>
</div>
<div class="quote-mark" style="left:259px">“</div>
<div class="quote-mark" style="left:582px">“</div>
<div class="quote-mark" style="left:904px">“</div>
<div class="dots small" style="left:592px;top:4270px"><i></i><i></i><i></i><i></i></div>

<!-- quote form -->
<svg class="layer" style="top:4330px" width="1200" height="600" viewBox="0 0 1200 600" role="img" aria-label="Faded photo backdrop in warm brown tones">
  <defs><linearGradient id="formFill" x1="0" y1="0" x2="1" y2="1"><stop offset="0" stop-color="#9a7f5e"/><stop offset=".5" stop-color="#876949"/><stop offset="1" stop-color="#7a5d3e"/></linearGradient></defs>
  <path d="M0 70 C120 20 260 0 380 20 C520 45 640 110 800 110 C950 110 1080 80 1200 60 L1200 590 L0 590 Z" fill="url(#formFill)"/>
  <path d="M0 560 L90 555 L180 566 L300 552 L430 565 L560 553 L700 566 L840 554 L980 565 L1100 553 L1200 562 L1200 600 L0 600 Z" fill="#000"/>
</svg>
<h2 class="abs form-title">Get a Free Quote</h2>
<div class="field line" style="top:4584px">Name:</div>
<div class="field line" style="top:4653px">Email:</div>
<div class="field line" style="top:4727px">Phone:</div>
<div class="field msg">Message</div>
<div class="abs round-btn submit">Submit<br>Here</div>

<!-- footer -->
<div class="abs" style="left:0;top:4920px;width:1200px;height:345px;background:var(--black)"></div>
<div class="abs foot-brand">
  <div class="brand-mark"></div>
  <div class="brand-name">HOLLOWAY<br><span style="font-size:18px;letter-spacing:4px">COATINGS</span></div>
</div>
<div class="abs foot-head" style="left:443px;top:4978px">Contact</div>
<ul class="abs contact-list">
  <li style="top:0"><span class="icon-dot"><svg width="12" height="14" viewBox="0 0 24 28"><path fill="#fff" d="M12 0a9 9 0 0 0-9 9c0 7 9 19 9 19s9-12 9-19a9 9 0 0 0-9-9zm0 12a3 3 0 1 1 0-6 3 3 0 0 1 0 6z"/></svg></span><span>Rowan Hale<br>Kestrel Bay, Northvale.</span></li>
  <li style="top:73px"><span class="icon-dot"><svg width="13" height="13" viewBox="0 0 24 24"><path fill="#fff" d="M6.6 10.8a15 15 0 0 0 6.6 6.6l2.2-2.2c.3-.3.7-.4 1-.2 1.1.4 2.3.6 3.6.6.6 0 1 .4 1 1V20c0 .6-.4 1-1 1A17 17 0 0 1 3 4c0-.6.4-1 1-1h3.5c.6 0 1 .4 1 1 0 1.3.2 2.5.6 3.6.1.3 0 .7-.2 1z"/></svg></span><span>Phone: 022 555 0148</span></li>
  <li style="top:119px"><span class="icon-dot"><svg width="13" height="10" viewBox="0 0 24 18"><rect x="1" y="1" width="22" height="16" fill="none" stroke="#fff" stroke-width="2"/><path d="M1 1l11 9 11-9" fill="none" stroke="#fff" stroke-width="2"/></svg></span><span>Email: hello@hollowaycoatings.co.nz</span></li>
</ul>
<div class="abs foot-head" style="left:800px;top:4978px">Sponsored By</div>
<div class="partner" style="left:800px;top:5036px;width:126px;background:#1f3f8f;display:flex;align-items:center;justify-content:center;color:#fff;font-size:22px;font-weight:600">Velnor</div>
<div class="partner" style="left:800px;top:5088px;width:240px;height:44px;background:#2aa3d9"></div>
<div class="social" style="left:793px"></div>
<div class="social" style="left:833px"></div>
<div class="social" style="left:873px"></div>
<div class="social" style="left:913px"></div>
<div class="abs copyright">© 2022 Holloway Coatings,All Rights Reserved</div>

</body>
</html>
```